Brenton Wealth Management Flow Charts

I need help creating three flow charts for my businesses website. We want them to be simple but look professional. This is for a Wealth Management firm. I will attach a word document that has all of the descriptions for everything so you know what icons to use. We just want the chart to have an icon, the names of each step and the corresponding numbers. I will also include some examples of charts we liked as well. Once the winner is selected, we will need help with additional graphic design elements for our website ASAP.
- Goudy Roman

```html
<!DOCTYPE html>
<html lang="en">
<head>
<meta charset="utf-8">
<title>Brenton Wealth Management Flow Charts</title>
<link rel="stylesheet" href="https://fonts.googleapis.com/css2?family=Sorts+Mill+Goudy&family=Lato:wght@400;700&display=swap">
<style>
  :root{
    --ink:#2f3136;
    --muted:#6d6f73;
    --rule:#8a8c90;
    --step-1:#3a3d42;
    --step-2:#5b7fa6;
    --step-3:#4e7a3c;
    --step-4:#d6a826;
    --step-5:#d9791f;
    --step-6:#b23a22;
    --page:#ffffff;
  }
  *{box-sizing:border-box;margin:0;padding:0}
  html,body{width:729px;height:1200px;overflow:hidden;background:var(--page)}
  .canvas{position:relative;width:729px;height:1200px}
  .chart-panel{
    position:absolute;left:14px;width:700px;height:345px;
    background:linear-gradient(180deg,#ffffff 0%,#f6f6f6 100%);
    border:1px solid #e2e2e2;box-shadow:0 2px 8px rgba(0,0,0,.12);overflow:hidden;
  }
  .chart-panel.retirement{top:95px}
  .chart-panel.investment{top:465px}
  .chart-panel.legacy{top:840px}
  .chart-title{
    position:absolute;left:18px;top:14px;
    font-family:"Sorts Mill Goudy",serif;font-size:20px;font-weight:400;letter-spacing:.5px;color:var(--ink);
  }
  .title-rule{position:absolute;left:18px;top:42px;width:400px;height:1px;background:var(--rule)}
  .theme-badge{position:absolute;left:37px;top:55px;width:76px;height:76px;border-radius:50%;background:radial-gradient(circle at 40% 35%,#4a4d52,#26282c)}
  .staircase{position:absolute;left:0;top:0;width:700px;height:345px}
  .intro-note{
    position:absolute;left:190px;top:50px;width:200px;
    font-family:Lato,sans-serif;font-size:7px;line-height:1.4;color:var(--muted);
  }
  .step{position:absolute;width:80px;text-align:center;font-family:Lato,sans-serif;transform:translate(-50%,-100%)}
  .step-name{font-family:"Sorts Mill Goudy",serif;font-size:9.5px;letter-spacing:.4px;text-transform:uppercase;line-height:1.15;color:var(--ink)}
  .step-note{margin-top:3px;font-size:6.5px;line-height:1.35;color:var(--muted)}
  .step-heart{display:block;width:10px;height:10px;margin:4px auto 0}
  .c1{--c:var(--step-1)} .c2{--c:var(--step-2)} .c3{--c:var(--step-3)}
  .c4{--c:var(--step-4)} .c5{--c:var(--step-5)} .c6{--c:var(--step-6)}
  .step-heart path{fill:var(--c)}
  .brand{position:absolute;left:505px;top:255px;display:flex;align-items:center;gap:8px;font-family:"Sorts Mill Goudy",serif;color:var(--ink)}
  .brand-square{width:13px;height:13px;background:var(--ink)}
  .brand-name{font-size:12px;letter-spacing:1px;text-transform:uppercase;line-height:1.25;white-space:nowrap}
  .sheen{position:absolute;left:40px;right:40px;bottom:8px;height:12px;border-radius:50%;
    background:linear-gradient(90deg,rgba(91,127,166,.18),rgba(78,122,60,.18),rgba(214,168,38,.18),rgba(178,58,34,.18));filter:blur(4px)}
</style>
</head>
<body>
<svg width="0" height="0" style="position:absolute" aria-hidden="true">
  <defs>
    <symbol id="stairs" viewBox="0 0 700 345">
      <g fill="none" stroke-width="30" stroke-linejoin="miter" stroke-linecap="butt">
        <polyline points="40,270 95,310 150,242" stroke="#3a3d42"/>
        <polyline points="150,242 205,282 260,214" stroke="#5b7fa6"/>
        <polyline points="260,214 315,254 370,186" stroke="#4e7a3c"/>
        <polyline points="370,186 425,226 480,158" stroke="#d6a826"/>
        <polyline points="480,158 535,198 590,130" stroke="#d9791f"/>
        <polyline points="590,130 640,170 685,102" stroke="#b23a22"/>
      </g>
      <g fill="#ffffff" stroke="rgba(0,0,0,.15)" stroke-width="1">
        <circle cx="122" cy="276" r="9"/><circle cx="232" cy="248" r="9"/>
        <circle cx="342" cy="220" r="9"/><circle cx="452" cy="192" r="9"/>
        <circle cx="562" cy="164" r="9"/><circle cx="662" cy="136" r="9"/>
      </g>
      <g fill="#6d6f73">
        <circle cx="122" cy="276" r="3"/><circle cx="232" cy="248" r="3"/>
        <circle cx="342" cy="220" r="3"/><circle cx="452" cy="192" r="3"/>
        <circle cx="562" cy="164" r="3"/><circle cx="662" cy="136" r="3"/>
      </g>
    </symbol>
    <symbol id="heart" viewBox="0 0 10 10"><path d="M5 9 L1 5 A2.2 2.2 0 0 1 5 2 A2.2 2.2 0 0 1 9 5 Z"/></symbol>
  </defs>
</svg>

<main class="canvas">
  <section class="chart-panel retirement">
    <h2 class="chart-title">THE RETIREMENT PLANNING PROCESS</h2>
    <div class="title-rule"></div>
    <div class="theme-badge" role="img" aria-label="Round badge with a palm tree and sunset icon for retirement"></div>
    <div class="sheen"></div>
    <svg class="staircase"><use href="#stairs"/></svg>
    <div class="step c1" style="left:95px;top:238px"><div class="step-name">Discovery<br>Meeting</div><p class="step-note">We listen to your goals first.</p><svg class="step-heart"><use href="#heart"/></svg></div>
    <div class="step c2" style="left:205px;top:210px"><div class="step-name">Learning</div><p class="step-note">We study your full financial picture.</p><svg class="step-heart"><use href="#heart"/></svg></div>
    <div class="step c3" style="left:315px;top:182px"><div class="step-name">Planning</div><p class="step-note">A clear plan built around you.</p><svg class="step-heart"><use href="#heart"/></svg></div>
    <div class="step c4" style="left:425px;top:154px"><div class="step-name">Execution</div><p class="step-note">We put each plan step in motion.</p><svg class="step-heart"><use href="#heart"/></svg></div>
    <div class="step c5" style="left:535px;top:126px"><div class="step-name">Adjustment</div><p class="step-note">Changes in life shape new choices.</p><svg class="step-heart"><use href="#heart"/></svg></div>
    <div class="step c6" style="left:638px;top:92px"><div class="step-name">Review</div><p class="step-note">Regular check-ins keep you on track.</p><svg class="step-heart"><use href="#heart"/></svg></div>
    <div class="brand"><span class="brand-square"></span><span class="brand-name">Brenton<br>Wealth Management</span></div>
  </section>

  <section class="chart-panel investment">
    <h2 class="chart-title">COMPREHENSIVE INVESTMENT MANAGEMENT</h2>
    <div class="title-rule" style="width:440px"></div>
    <div class="theme-badge" role="img" aria-label="Round badge with a piggy bank icon for investing"></div>
    <div class="sheen"></div>
    <svg class="staircase"><use href="#stairs"/></svg>
    <div class="step c1" style="left:95px;top:238px"><div class="step-name">Understanding<br>Your Risk<br>Tolerance</div><p class="step-note">We gauge your comfort with risk.</p><svg class="step-heart"><use href="#heart"/></svg></div>
    <div class="step c2" style="left:205px;top:210px"><div class="step-name">Investment<br>Selection</div><p class="step-note">Holdings chosen to suit your plan.</p><svg class="step-heart"><use href="#heart"/></svg></div>
    <div class="step c3" style="left:315px;top:182px"><div class="step-name">Asset<br>Allocation</div><p class="step-note">Balanced mix across asset classes.</p><svg class="step-heart"><use href="#heart"/></svg></div>
    <div class="step c4" style="left:425px;top:154px"><div class="step-name">Tax<br>Efficiency</div><p class="step-note">Keeping more of what you earn.</p><svg class="step-heart"><use href="#heart"/></svg></div>
    <div class="step c5" style="left:535px;top:126px"><div class="step-name">Distribution<br>Strategy</div><p class="step-note">Steady income for your later years.</p><svg class="step-heart"><use href="#heart"/></svg></div>
    <div class="step c6" style="left:638px;top:92px"><div class="step-name">Behavior<br>Finance Coaching</div><p class="step-note">Calm guidance through market swings.</p><svg class="step-heart"><use href="#heart"/></svg></div>
    <div class="brand"><span class="brand-square"></span><span class="brand-name">Brenton<br>Wealth Management</span></div>
  </section>

  <section class="chart-panel legacy">
    <h2 class="chart-title">LEGACY AND ESTATE PLANNING</h2>
    <div class="title-rule" style="width:330px"></div>
    <p class="intro-note">Your legacy is more than wealth. We help you pass on what matters most to the people and causes you love.</p>
    <div class="theme-badge" role="img" aria-label="Round badge with a family tree icon for legacy"></div>
    <div class="sheen"></div>
    <svg class="staircase"><use href="#stairs"/></svg>
    <div class="step c2" style="left:205px;top:210px"><div class="step-name">Beneficiaries</div><p class="step-note">Name who receives your assets.</p><svg class="step-heart"><use href="#heart"/></svg></div>
    <div class="step c3" style="left:315px;top:182px"><div class="step-name">Trusts</div><p class="step-note">Trusts that protect your family.</p><svg class="step-heart"><use href="#heart"/></svg></div>
    <div class="step c4" style="left:425px;top:154px"><div class="step-name">Estate Taxes<br>&amp; Inheritance</div><p class="step-note">Planning to ease taxes for heirs.</p><svg class="step-heart"><use href="#heart"/></svg></div>
    <div class="step c5" style="left:535px;top:126px"><div class="step-name">Annual<br>Giving</div><p class="step-note">Yearly gifts made with purpose.</p><svg class="step-heart"><use href="#heart"/></svg></div>
    <div class="step c6" style="left:638px;top:92px"><div class="step-name">Donations<br>&amp; Charity</div><p class="step-note">Support the causes you care for.</p><svg class="step-heart"><use href="#heart"/></svg></div>
    <div class="brand"><span class="brand-square"></span><span class="brand-name">Brenton<br>Wealth Management</span></div>
  </section>
</main>
</body>
</html>
```